Medical Breast Thermography Brochure Needed

Looking for a brochure that matches the theme and overall look/feel of our website brookhavenhc.com.

http://brookhavenhc.com/ourservices/breast-thermography/

I have previously used PixelMarket for logo, business card, and brochure and have been very happy, as soon as designs start being submitted I will switch to guaranteed payment.

I'm looking for a professional, clean, simple, minimalist, bold design.
Colors would ideally be greens and blues, or pink, cool tones, muted colors, or graytones.

See attached word document for content for brochure.

I would like to have the TH1-TH5 images in the Corvane thermo brochure 11.pdf document in the brochure.

Also would like one fold to compare mammogram with breast thermography like in BKHC_thermography_vs_mammography.jpg

I have attached a copy of our prior overall practice brochure to see what type of design I would like.

Feel free to use any stock photos.

```html
<!DOCTYPE html>
<html lang="en">
<head>
<meta charset="utf-8">
<title>Brookhaven Health Care – Breast Thermography Brochure</title>
<link href="https://fonts.googleapis.com/css2?family=Source+Sans+3:ital,wght@0,400;0,600;0,700;1,400;1,600&family=Roboto+Slab:wght@300;400&family=Oswald:wght@500&display=swap" rel="stylesheet">
<style>
:root{
  --green:#6aa535;
  --pink:#d6246e;
  --blue:#2a8ccf;
  --navy:#1d5f91;
  --ink:#333;
  --soft:#eaf3fa;
  --bg:#d9dcdf;
  --photo-skin-top:#f3e6dc;
  --photo-skin-bottom:#e4cbb8;
  --photo-scan-a:#5b86b8;
  --photo-scan-b:#7fae8c;
  --figure-grey:#4a4a4a;
}
*{margin:0;padding:0;box-sizing:border-box}
html,body{width:1200px;height:1200px;overflow:hidden;background:var(--bg)}
body{font-family:"Source Sans 3",sans-serif;color:var(--ink);position:relative}
.spread{position:absolute;left:228px;width:744px;height:576px;display:flex;box-shadow:0 2px 8px rgba(0,0,0,.25)}
.spread.outside{top:16px}
.spread.inside{top:608px}
.panel{position:relative;width:248px;height:100%;overflow:hidden;
  background:linear-gradient(180deg,#fff 0%,var(--soft) 55%,#fff 100%);padding:18px 18px 0 20px;
  font-style:italic}
.outside .panel{font-size:6.5px;line-height:1.42}
.inside .panel{font-size:6.4px;line-height:1.4}
.panel + .panel{border-left:1px solid #d4dde4}
p{margin-bottom:4px;text-align:justify}
h2{font-style:normal;font-weight:700;font-size:8.4px;line-height:1.22;margin:8px 0 3px}
h2.pink{color:var(--pink)} h2.blue{color:var(--navy)}
h3{font-style:italic;font-weight:600;color:var(--blue);font-size:6.6px;margin:4px 0 2px}
ol.numbered{list-style:none;counter-reset:n 3}
ol.numbered li{counter-increment:n;position:relative;padding-left:10px;margin-bottom:4px;text-align:justify}
ol.numbered li::before{content:counter(n) ".";position:absolute;left:0;color:var(--blue);font-style:normal;font-weight:700}
ol.facts{counter-reset:n 0}
ul.dots{list-style:none}
ul.dots li{position:relative;padding-left:10px;margin-bottom:2.5px;text-align:justify}
ul.dots li::before{content:"";position:absolute;left:1px;top:2.6px;width:3.5px;height:3.5px;border-radius:50%;background:var(--pink)}
ul.dots.blue-text li{color:var(--blue)}
ul.dots li.plain{color:var(--ink)}
ul.ticks{list-style:none}
ul.ticks li{position:relative;padding-left:10px;margin-bottom:2.5px;text-align:justify}
ul.ticks li::before{content:"";position:absolute;left:0;top:1.6px;width:5px;height:5px;border:.8px solid var(--pink);border-radius:50%}
ul.ticks li::after{content:"";position:absolute;left:1.7px;top:2.9px;width:1.6px;height:1px;border-left:.8px solid var(--pink);border-bottom:.8px solid var(--pink);transform:rotate(-45deg)}
.clinic-box{background:var(--blue);color:#fff;margin:8px -18px 6px -20px;padding:6px 18px 6px 20px}
.clinic-box b{font-style:normal}
.closing{color:var(--pink);font-style:normal;font-weight:700;font-size:8px;margin-top:6px}
.cost-title{font-family:"Roboto Slab",serif;color:var(--pink);font-size:11.5px;text-align:center;letter-spacing:1px;font-style:normal;margin-bottom:4px}
table.fees{width:100%;border-collapse:collapse;font-style:normal;font-size:6px;margin:6px 0 12px;border:.8px solid var(--green)}
table.fees th{background:var(--green);color:#fff;font-weight:400;padding:2px 3px;font-size:5.2px}
table.fees td{border:.6px solid #b9c6b0;padding:3.4px 3px;background:#fff;vertical-align:middle}
table.fees td:first-child{text-align:center;width:16%}
table.fees td:last-child{text-align:center;width:16%}
.slab{font-family:"Roboto Slab",serif;font-style:normal;text-align:center}
.help-q{font-size:10px;color:#222;margin-top:4px}
.help-a{font-size:10px;color:var(--pink);margin-bottom:8px}
.quality{font-family:"Roboto Slab",serif;font-style:normal;font-weight:300;font-size:11.6px;line-height:1.35;color:#444;margin:10px 0}
.quality b{font-weight:400}
.call{font-family:"Roboto Slab",serif;font-style:normal;color:var(--pink);font-size:11.6px;letter-spacing:.4px}
.call-sub{font-family:"Roboto Slab",serif;font-style:normal;font-size:10px;color:#333;margin-bottom:10px}
ul.contact{list-style:none;font-style:normal;font-size:7.6px;margin-bottom:10px}
ul.contact li{display:flex;align-items:center;gap:8px;margin-bottom:6px}
ul.contact svg{width:11px;height:11px;fill:var(--navy)}
.hands{position:absolute;left:0;right:0;bottom:0;height:44px;background:linear-gradient(180deg,rgba(255,255,255,0),#dfe3e6)}
.bottom-arc{position:absolute;left:0;bottom:0;width:100%;height:18px}
.cover{padding:0}
.brand{position:absolute;top:40px;left:36px;right:10px;display:flex;align-items:center;gap:8px;white-space:nowrap}
.brand-dot{width:13px;height:13px;border-radius:50%;background:var(--blue);flex:none}
.brand-name{font-style:normal;font-weight:600;font-size:15px;color:var(--navy);letter-spacing:.3px}
.torso{position:absolute;top:96px;left:20px;right:0;height:330px;
  background:linear-gradient(180deg,var(--photo-skin-top) 0%,var(--photo-skin-bottom) 100%)}
.cover-arc{position:absolute;left:0;top:0;width:100%;height:100%}
.cover-text{position:absolute;left:40px;right:8px;top:424px;text-align:center;color:#fff;font-style:normal}
.cover-text .t1{font-family:"Roboto Slab",serif;font-size:24px;letter-spacing:1px;line-height:1}
.cover-text .t2{font-family:"Roboto Slab",serif;font-size:19px;margin-top:2px}
.cover-text .t3{font-family:"Roboto Slab",serif;font-size:11.4px;margin:10px 0 10px}
.cover-text .t4{font-size:9.4px;line-height:1.35}
.cover-text .t5{font-size:7.6px;letter-spacing:2.6px;margin-top:14px}
.intro-q{margin-top:4px}
.stat{display:flex;gap:8px;margin:4px 0 6px}
.stat-figure{width:92px;flex:none;font-style:normal}
.stat-people{height:22px;background:var(--figure-grey)}
.stat-big{font-family:"Oswald",sans-serif;color:var(--pink);font-size:15px;line-height:1.1;margin-top:3px;white-space:nowrap;letter-spacing:-.3px}
.stat-small{font-family:"Oswald",sans-serif;font-size:5.4px;color:#222;white-space:nowrap}
.stat-text h2{margin:0 0 2px;color:var(--pink);font-size:7.8px}
.solution{font-style:normal;font-weight:600;color:var(--navy);font-size:8.4px;line-height:1.25;margin:6px 0 4px}
.scans{position:absolute;bottom:20px;left:26px;display:flex;gap:18px}
.scan{width:88px;height:88px;border-radius:50%;border:4px solid var(--pink);
  background:linear-gradient(160deg,var(--photo-scan-a),var(--photo-scan-b))}
.benefits{border:.8px solid #b7c9d8;background:#fff;padding:5px 7px;margin:8px 0 6px;font-style:normal}
.benefits h2{margin:0 0 3px;color:var(--pink)}
.benefits ul{display:flex;flex-wrap:wrap;column-gap:12px}
.benefits li{margin-bottom:2px}
.chart{border:.8px solid #b7c9d8;background:#fff;height:64px;margin:6px 0;position:relative}
.chart svg{width:100%;height:100%}
</style>
</head>
<body>

<section class="spread outside">
  <div class="panel">
    <ol class="numbered">
      <li>Many false negatives occur with mammograms since tumors are frequently located in the upper outer aspects of the breasts where the scans do not reach.</li>
      <li>In Europe, Canada, &amp; Australia healthy breasts are routinely screened with thermography and mammograms are used as a second line of diagnosis.</li>
      <li>For earliest detection and prevention, it is recommended that women receive baseline breast thermography at age 20, every three years between ages 20-30, and annually from age 30.</li>
      <li>Starting breast thermography at any age gives you the safest and earliest detection possible.</li>
    </ol>
    <h2 class="pink">What are the SIDE EFFECTS of Breast Thermography?</h2>
    <p>There are no known short or long-term side effects of breast thermography. It is incredibly safe!</p>
    <h2 class="blue">HOW SHOULD I PREPARE for my Breast Thermography appointment?</h2>
    <p>Prior to the test, please adhere to the following:</p>
    <ul class="dots">
      <li>No natural or artificial tanning 5 days prior to your test date</li>
      <li>No breast manipulation prior to the test, including breast self-exams, compression of the breasts, breast stimulation, breast ultrasound, or mammogram for 24h prior to the test</li>
      <li>No fevers for at least 36h prior to the test</li>
      <li>No steam rooms, saunas, heat packs, or cold packs for at least 4 hours prior to the test</li>
      <li>Do not shave your underarms or use skin creams, lotions, deodorants, or powders on your breast before your test</li>
      <li>No coffee, tea, or tobacco two hours before the test</li>
      <li>No restrictive clothing</li>
    </ul>
    <div class="clinic-box"><b>AT THE CLINIC :</b> Arrive a few minutes early to your appointment. Your body will take time to adjust to the temperature of the clinic. You will be disrobing down to your underwear of choice. You will meet your thermographer who will explain and demonstrate the required views and positions necessary for your exam. Thermal images are then taken of either the whole body or just the regions of interest. A cold "stress" test is performed with this test, which simply involves placing a hand or foot in a cool bowl of water.</div>
    <h2 class="pink" style="margin-top:4px">How long will my appointment last?</h2>
    <p>Your appointment will last 30-60 minutes.</p>
    <h2 class="blue" style="margin-top:4px">When will I get my results?</h2>
    <p>Our board certified Physician evaluates each thermographic image and creates a report. Your comprehensive interpretive report, including images, will be ready to follow up within a 7-14 Business days.</p>
    <p>Our goal is to educate the community to consider thermography when it comes to their health. Some patients ask us to perform a yearly analysis to identify any changes or possible areas of concern. We understand medical testing can be cause of anxiety. We aim to make you experience as pleasant and comfortable as possible.</p>
    <div class="closing">SO WHAT DO YOU THINK?</div>
    <svg class="bottom-arc" viewBox="0 0 248 18" preserveAspectRatio="none"><path d="M0 18 L0 12 Q140 6 248 0 L248 18Z" fill="var(--blue)"/><path d="M0 18 L0 16 Q150 10 248 5 L248 18Z" fill="#fff"/></svg>
  </div>

  <div class="panel">
    <div class="cost-title">COST</div>
    <p style="font-style:normal">Thermography is not yet paid by insurance companies. For this reason, we consider this an alternative service, not requiring a doctor's order and payable at the time of service. Current rates are as follows:</p>
    <table class="fees">
      <tr><th>Procedure Code</th><th>Description</th><th>Standard Fee</th></tr>
      <tr><td>THBRA</td><td>Thermogram Breast, Annual</td><td>$200.00</td></tr>
      <tr><td>THRO1</td><td>Thermogram 1 Region of Interest (Head, Abdomen, Lower extremities, Upper extremities)</td><td>$180.00</td></tr>
      <tr><td>THROB</td><td>Thermogram 1 Region of Interest With Breasts</td><td>$250.00</td></tr>
      <tr><td>THMHS</td><td>Men's Screen (includes head, neck, thyroid, chest, abdomen, upper and lower back)</td><td>$275.00</td></tr>
      <tr><td>THWHS</td><td>Women's Screen (includes head, neck, thyroid, breast, abdomen/pelvis, upper and lower back)</td><td>$325.00</td></tr>
      <tr><td>THPS</td><td>Thermogram Cervical or Lumbar Study, 3 Sets of images</td><td>$350.00</td></tr>
    </table>
    <div class="slab help-q">Already had Breast Thermography?</div>
    <div class="slab help-a">WE NEED YOUR HELP!</div>
    <p>If you have already had Breast Thermography at Brookhaven Health Care we would love it if you could share your feedback about your experience. Your feedback is incredibly valuable and will be able to help thousands of people determine if breast thermography is right for them. Simply send us an email with your feedback today!</p>
    <div class="quality">We provide the <b>highest quality</b> imaging and <b>affordable pricing!</b></div>
    <div class="call">CALL TODAY TO SCHEDULE</div>
    <div class="call-sub">your thermography with our office</div>
    <ul class="contact">
      <li><svg viewBox="0 0 24 24"><path d="M6.6 10.8a15 15 0 006.6 6.6l2.2-2.2c.3-.3.7-.4 1-.2 1.1.4 2.3.6 3.6.6.6 0 1 .4 1 1V20c0 .6-.4 1-1 1A17 17 0 013 4c0-.6.4-1 1-1h3.5c.6 0 1 .4 1 1 0 1.3.2 2.5.6 3.6.1.3 0 .7-.2 1z"/></svg>(555) 214-7730 (Brookhaven)</li>
      <li><svg viewBox="0 0 24 24"><path d="M6 2h10v6H6zM3 9h18v11H3zm3 3v2h4v-2zm0 4v2h4v-2zm8-4v6h4v-6z"/></svg>(555) 214-7731</li>
      <li><svg viewBox="0 0 24 24"><path d="M12 2a10 10 0 100 20 10 10 0 000-20zm6.9 6h-3a15 15 0 00-1.3-3.9A8 8 0 0118.9 8zM12 4c.8 1.2 1.5 2.5 1.9 4h-3.8c.4-1.5 1.1-2.8 1.9-4zM4.3 14a8 8 0 010-4h3.4a16 16 0 000 4zm.8 2h3a15 15 0 001.3 3.9A8 8 0 015.1 16zm3-8h-3a8 8 0 014.3-3.9C8.8 5.3 8.4 6.6 8.1 8zM12 20c-.8-1.2-1.5-2.5-1.9-4h3.8c-.4 1.5-1.1 2.8-1.9 4zm2.3-6H9.7a14 14 0 010-4h4.6a14 14 0 010 4zm.3 5.9c.6-1.2 1-2.5 1.3-3.9h3a8 8 0 01-4.3 3.9zm1.7-5.9a16 16 0 000-4h3.4a8 8 0 010 4z"/></svg>www.brookhavenhc.com</li>
      <li><svg viewBox="0 0 24 24"><path d="M12 3L2 12h3v8h5v-5h4v5h5v-8h3z"/></svg>480 Meadow Crest Dr. Fairview, TX 79000</li>
    </ul>
    <p style="font-style:normal">1in8 get breast cancer you don't have to be one of them. Call today to let us help you minimize your breast cancer risk and optimize your health.</p>
    <div class="hands" role="img" aria-label="Soft photograph of hands resting on fabric"></div>
  </div>

  <div class="panel cover">
    <div class="brand"><span class="brand-dot"></span><span class="brand-name">Brookhaven Health Care</span></div>
    <div class="torso" role="img" aria-label="Photograph of a woman's bare torso with hands covering her breasts"></div>
    <svg class="cover-arc" viewBox="0 0 248 576" preserveAspectRatio="none">
      <path d="M12 576 Q0 300 60 160 Q140 50 248 70" fill="none" stroke="var(--pink)" stroke-width="1.4"/>
      <path d="M24 576 Q12 470 70 420 Q150 360 248 380 L248 576Z" fill="var(--green)"/>
    </svg>
    <div class="cover-text">
      <div class="t1">BREAST</div>
      <div class="t2">Thermography</div>
      <div class="t3">Safe Screening. Early Detection</div>
      <div class="t4">Now you don't have to wait till your next mammogram to get a window into your breast health!</div>
      <div class="t5">WWW.BROOKHAVENHC.COM</div>
    </div>
  </div>
</section>

<section class="spread inside">
  <div class="panel">
    <p>Whether you are a busy mom of three, a retired grandmother, or a working woman, your health is your most valuable asset, and you try your best to be on top of taking care of your health.</p>
    <p class="intro-q">So, what about your breast health?<br>Have you had your breast-health checked recently?</p>
    <h2 class="pink">Perhaps you:</h2>
    <ul class="ticks">
      <li>Have a family history of breast cancer but are too young for a mammogram</li>
      <li>Are worried about toxic radiation exposure from mammograms</li>
      <li>You have had surgery, implants, or biopsies that might make mammograms difficult to interpret</li>
      <li>Have had an inconclusive mammogram</li>
      <li>Are just plain worried about your breast health</li>
    </ul>
    <div class="solution">No matter which situation you are in, Brookhaven Health Care has the perfect solution for you!</div>
    <div class="stat">
      <div class="stat-figure">
        <div class="stat-people" role="img" aria-label="Row of eight women figures, one highlighted in pink"></div>
        <div class="stat-big">1 IN 8 WOMEN</div>
        <div class="stat-small">WILL DEVELOP BREAST CANCER</div>
      </div>
      <div class="stat-text">
        <h2>WHY Breast Health?</h2>
        <p>As you already know, breast health is incredibly important, and breast problems can develop silently for decades before anything can be picked up on a mammogram!</p>
      </div>
    </div>
    <ul class="dots">
      <li>Every 2 minutes a woman is diagnosed with Breast Cancer</li>
      <li>Every 13 minutes a woman in the US loses her life to breast cancer</li>
      <li>More than 250,000 women under 40 in the US live with a breast cancer diagnosis</li>
      <li>About one in eight women in the U.S. will develop invasive breast cancer during her lifetime.</li>
      <li>Breast cancer is the most common cancer in American women, behind skin cancer, and second-leading cause of cancer death in women, exceeded only by lung cancer.</li>
      <li>An estimated 232,670 new cases of invasive breast cancer will be diagnosed in U.S. women this year.</li>
      <li>Two of three breast cancers are found in women 55 or older and approximately <b>1/3</b> of all breast cancers occur in women <b>under 45.</b></li>
      <li>Here at Brookhaven Health Care, we don't just deal with problems after they have formed. We pride ourselves on comprehensive, preventive health-care to keep you happy and healthy, and this is why we have developed a comprehensive Breast Health Screening Program using state-of-the-art <b>Breast Thermography.</b></li>
    </ul>
    <div class="scans">
      <div class="scan" role="img" aria-label="Thermal scan image of a torso"></div>
      <div class="scan" role="img" aria-label="Thermal scan image of a torso"></div>
    </div>
  </div>

  <div class="panel">
    <h2 class="pink" style="margin-top:0">WHAT IS Breast Thermography?</h2>
    <p>Breast Thermography is an exciting addition to breast imaging technology that was approved by the FDA in 1982. It is an additional tool that doctors use to help determine breast cancer risk and can also indicate the risk of other breast conditions. When Breast Thermography is used in combination with other tests, it gives your doctor an improved overall picture of breast health.</p>
    <p>Breast Thermography uses infra-red imaging technology to scan the breast and produces an incredibly detailed heat map, which can help detect the new blood vessels that grow from tumors, as well as hormonal imbalances, and other breast-health problems.</p>
    <p>Breast thermography provides an additional piece of the puzzle and is not to be used alone. However, when used together with other imaging and lab tests, it will provide your doctor with much more information, giving a more comprehensive picture of your overall breast health.</p>
    <div class="benefits">
      <h2>BENEFITS OF Breast Thermography</h2>
      <ul class="ticks">
        <li>Safe</li><li>Painless</li><li>No harmful radiation</li><li>Fast</li>
        <li>Can be used at any age</li>
        <li>No limit on number of tests you can have per year</li>
      </ul>
    </div>
    <h2 class="pink">WHO SHOULD HAVE Breast Thermography?</h2>
    <h3>Women with Fibrocystic Breasts or Dense Breasts</h3>
    <ul class="ticks"><li>Dense breast tissue contains more glands and ligaments and less fat. Mammograms have trouble seeing through dense tissue; however thermograms can easily evaluate dense breast tissue.</li></ul>
    <h3>Women with inconclusive mammograms</h3>
    <ul class="ticks"><li>Thermography can reduce the need for biopsies by up to 20%.</li></ul>
    <h3>Women with surgical implants</h3>
    <ul class="ticks"><li>The risk of an implant rupturing during a mammogram is a small, but valid concern. With thermography there is no compression and no risk!</li></ul>
    <h3>Younger women who want to limit radiation exposure to the breast</h3>
    <ul class="ticks"><li>A routine mammogram consists of two views of each breast and contains up to 0.2 rad per x-ray. Radiation accumulates in breast tissue, and each 1.0 rad of exposure increases the risk of breast cancer by 1 percent. Because thermography images thermal heat emanating from the body, there is no radiation risk whatsoever.</li></ul>
    <h3>Women with a family history of breast cancer</h3>
    <ul class="ticks"><li>Annual breast screening is not usually recommended until age 40; however, if you fall into the high risk category, thermograms should be started in the mid 20's in order to obtain a baseline for all future comparisons.</li></ul>
    <ul class="dots blue-text" style="margin-top:4px">
      <li>Women struggling with hormone imbalance</li>
      <li class="plain">Women who want a baseline for overall breast health</li>
      <li>Women who have had surgical procedures or biopsies to the breast</li>
      <li class="plain">Women who have had a mastectomy</li>
      <li>You have had an abnormal mammogram and have been told you need to wait 6 months before your next mammogram</li>
      <li class="plain">Any man or woman concerned about breast health</li>
    </ul>
  </div>

  <div class="panel">
    <h2 class="pink" style="margin-top:0">WHAT IS THE DIFFERENCE BETWEEN<br><span style="color:var(--navy)">a Mammogram and Breast Thermography?</span></h2>
    <p>Unlike a mammogram, which is used to diagnose breast cancer by using X-Rays that find denser tissues, a Breast Thermography Machine uses Infra-Red Imaging to find "hotter" areas of the breast that are more active.</p>
    <p>A Mammogram is like taking a still photograph that tells you how a breast looks.</p>
    <p>Breast Thermography is like actively looking through a set of infra-red heat goggles that can tell you how the breast is working.</p>
    <p>Both tests give us different information and are both important when it comes to assessing your breast health.</p>
    <h2 class="pink">FREQUENTLY ASKED QUESTIONS:</h2>
    <h2 class="blue" style="margin-top:0">Can I use Breast Thermography instead of a mammogram to diagnose breast cancer?</h2>
    <p>No. When it comes to a breast cancer diagnosis, a breast biopsy is the gold-standard for diagnosing breast cancer.</p>
    <p>Breast Thermography is used together with other tests including mammograms, ultrasounds, MRI's, blood testing, and genetic testing, in order to add incredible amounts of detail to generate a comprehensive picture of your breast health and your risk of breast cancer.</p>
    <h2 class="pink">Thermography? Mammograms? Or both?</h2>
    <p>By the time a tumor reaches the size of a pin head (approximately two years into its growth) it can no longer be sustained by the normal blood supply and so it develops its own. The development of that blood supply is called angiogenesis. Thermography is the only technology in place that can detect angiogenesis.</p>
    <div class="chart">
      <svg viewBox="0 0 212 64" font-family="Source Sans 3, sans-serif" font-size="3.6">
        <circle cx="36" cy="20" r="1.8" fill="var(--pink)"/><circle cx="54" cy="20" r="1.8" fill="var(--pink)"/>
        <circle cx="72" cy="20" r="3" fill="var(--blue)"/><circle cx="86" cy="20" r="4.2" fill="var(--blue)"/>
        <circle cx="110" cy="20" r="6.5" fill="var(--green)"/><circle cx="132" cy="20" r="8.5" fill="var(--green)"/>
        <circle cx="162" cy="20" r="11.5" fill="#27b3a3"/>
        <line x1="22" y1="40" x2="190" y2="40" stroke="#ccc" stroke-width=".5"/>
        <text x="26" y="46" font-weight="700">Infrared Thermography</text><text x="38" y="51">2mm</text>
        <text x="72" y="46">Screening MRI</text><text x="76" y="51">4-8mm</text>
        <text x="102" y="46">X-Ray Mammogram</text><text x="110" y="51">12-16mm</text>
        <text x="142" y="46">Breast Examination</text><text x="156" y="51">20mm</text>
      </svg>
    </div>
    <p>Mammogram is not early detection. A cancerous tumor has been growing eight to ten years before it is big enough and dense enough to be detected by mammography. That is why the treatment at that stage is so drastic – removal of breast, underlying muscle, lymph nodes, chemotherapy, radiation therapy and hormonal therapy.</p>
    <h2 class="pink">7 ADDITIONAL FACTS <span style="color:var(--navy)">about thermography vs. mammograms</span></h2>
    <ol class="numbered facts">
      <li>Breast thermography has been FDA approved as an adjunct diagnostic tool to mammograms since 1982.</li>
      <li>There have been 800 peer-reviewed breast thermography studies in which over a quarter million women have participated in large-scale studies over 12 years. These studies show thermography to be 90% accurate.</li>
      <li>Mammograms in pre-menopausal women can be up to 89% inaccurate, leading to unnecessary procedures, as well as emotional and physical trauma.</li>
    </ol>
  </div>
</section>

</body>
</html>
```